Corporate Comedy Poster Brochure

I have designed an 10.75 by 15 flat one-sided poster/flyer to mail out for promoting my corporate comedy services. I don't think I did a bad job, but would love to see if someone can create something else for the same purpose, but with an expert hand and eye, as I am not a designer by trade. You should get a sense of it by the PSD example I provided.

FYI: My websites are:
www.paulvantrimm.com/corporate-comedian
www.gigsforstaffnights.com

Target Market(s)

Event Planners, Chambers of Commerce, Human Resources people who might be in charge of the company party, Golf Courses, Banquet Facilities, etc.

Industry/Entity Type

Entertainment Industry

Font styles to use
Sans Serif

Requirements
Must have
• Must have the textual content, headshot, and all logos that are in the PSD I provided.
• 10.75 inches by 15 inches at 300dpi.
• The PSD is on my Stashbox Cloud at :https://files.stashboxcloud.com/file/d/7Kq41mzvtp3WyhaR8cLn2JsXeQ60/view?usp=sharing
• I promise there is no virus or you know who's website to take down, :-)
Nice to have
• 1) Would be nice to have final in Photoshop, as I could then make adjustments easier. I don't know Illustrator well.
• 2) My motif is a poster for a show that is really a flyer promoting the fact that I perform shows. You can stick with this motif, or if you have a better motif, I am open to that.

```html
<!DOCTYPE html>
<html lang="en">
<head>
<meta charset="utf-8">
<title>Comedy Night – Paul Vantrimm</title>
<link href="https://fonts.googleapis.com/css2?family=Bowlby+One&family=Anton&family=Oswald:wght@500;700&family=Open+Sans:ital,wght@0,400;0,700;1,400;1,700&display=swap" rel="stylesheet">
<style>
:root{
  --deep:#1c0303;
  --maroon:#4a0606;
  --red:#d8120c;
  --orange:#f28a12;
  --yellow:#ffd21a;
  --gold:#f5c400;
  --white:#ffffff;
  --ink:#1a1a1a;
  --suit:#1d2a44;
}
*{margin:0;padding:0;box-sizing:border-box}
html,body{width:861px;height:1200px;overflow:hidden}
body{
  position:relative;
  font-family:"Open Sans",sans-serif;
  color:var(--white);
  background:
    radial-gradient(ellipse 520px 360px at 430px 90px,#fff3a0 0%,var(--yellow) 18%,var(--orange) 42%,#a8200a 68%,transparent 90%),
    linear-gradient(180deg,var(--maroon) 0%,var(--deep) 55%,#0b0101 100%);
}
.poster-title{position:absolute;left:0;top:12px;width:861px;text-align:center}
.poster-title .comedy{
  display:block;
  font-family:"Bowlby One",sans-serif;
  font-size:145px;line-height:1;letter-spacing:2px;
  color:var(--red);
  -webkit-text-stroke:4px var(--yellow);
  text-shadow:0 6px 0 #6b0000;
}
.poster-title .night{
  display:block;margin-top:-4px;padding-left:240px;
  font-family:"Oswald",sans-serif;font-weight:700;font-style:italic;
  font-size:62px;letter-spacing:6px;line-height:1;color:var(--white);
}
.headshot{
  position:absolute;left:85px;top:205px;width:375px;height:485px;
  background:linear-gradient(180deg,#c98a6a 0%,#b07258 28%,#5c6e8e 40%,var(--suit) 62%,#10182a 100%);
  border-radius:180px 180px 0 0;
}
.tagline{
  position:absolute;left:465px;top:258px;width:385px;text-align:center;
  font-weight:700;font-size:22px;line-height:1.3;
}
.performer{
  position:absolute;left:465px;top:338px;width:385px;text-align:center;white-space:nowrap;
  font-family:"Anton",sans-serif;font-size:56px;line-height:1;
  color:var(--gold);-webkit-text-stroke:2px #6b3a00;letter-spacing:1px;
}
.credits{
  position:absolute;left:478px;top:420px;width:365px;height:62px;
  display:flex;justify-content:space-between;align-items:center;
}
.credit{
  display:flex;align-items:center;gap:5px;
  background:var(--white);border-radius:8px;padding:7px 8px;
  font-weight:700;font-size:12px;color:var(--ink);
}
.credit i{width:12px;height:12px;border-radius:50%;background:var(--red);display:block;flex:none}
.services{position:absolute;left:530px;top:505px;list-style:none}
.services li{
  display:flex;align-items:center;gap:14px;
  font-weight:700;font-size:23px;line-height:33px;color:var(--gold);
}
.services li::before{content:"";width:12px;height:12px;background:var(--gold);display:block}
.testimonials{
  position:absolute;left:15px;top:690px;width:440px;height:175px;
  background:var(--yellow);color:var(--ink);padding:14px 18px;
  font-size:14.5px;font-style:italic;line-height:1.3;
}
.testimonials blockquote{margin-bottom:10px}
.testimonials cite{display:block;text-align:right;font-weight:700;margin-top:4px}
.contact{
  position:absolute;left:465px;top:770px;width:381px;
  text-align:right;white-space:nowrap;font-size:19px;line-height:1.55;
}
.contact h3{font-size:20px;font-weight:700;margin-bottom:2px}
.event{
  position:absolute;left:22px;top:880px;
  font-family:"Anton",sans-serif;font-size:54px;line-height:1;
}
.clients-heading{
  position:absolute;left:22px;top:948px;
  font-weight:700;font-size:20px;color:var(--gold);
}
.clients{
  position:absolute;left:0;top:990px;width:861px;height:210px;
  background:var(--white);color:var(--ink);
  display:grid;grid-template-columns:repeat(6,1fr);grid-template-rows:1fr 1fr;
  align-items:center;padding:8px 12px;gap:4px 8px;
}
.client{
  display:flex;align-items:center;gap:5px;
  font-weight:700;font-size:13px;line-height:1.15;color:var(--ink);
}
.client i{width:11px;height:11px;background:var(--red);display:block;flex:none}
.clients .more{grid-column:span 2;font-size:12.5px;font-weight:400;text-align:center;line-height:1.25}
</style>
</head>
<body>
<header class="poster-title">
  <span class="comedy">COMEDY</span>
  <span class="night">NIGHT</span>
</header>

<div class="headshot" role="img" aria-label="Portrait of comedian Paul Vantrimm in a navy suit and blue shirt"></div>

<p class="tagline">Hilarious entertainment for any corporate, club or dinner event!</p>
<h1 class="performer">Paul Vantrimm</h1>

<div class="credits">
  <span class="credit"><i></i>Laugh Lane Live</span>
  <span class="credit"><i></i>Chuckle Channel</span>
  <span class="credit"><i></i>Orbitwave Radio</span>
</div>

<ul class="services">
  <li>Holiday Parties</li>
  <li>Awards Banquets</li>
  <li>Dinner Shows</li>
  <li>Country Clubs</li>
  <li>Community Shows</li>
  <li>Fundraisers</li>
</ul>

<section class="testimonials">
  <blockquote>"Your show was AMAZING!!! People were telling me for days how much fun they had and how great they thought you were."<cite>-Forward Mutual Insurance</cite></blockquote>
  <blockquote>"Paul, I can not tell you how well the evening went. This was the perfect first time comedy event."<cite>-Briarwood Country Club</cite></blockquote>
</section>

<section class="contact">
  <h3>For More Information:</h3>
  <p>Phone: 888-555-0142</p>
  <p>Website: www.paulvantrimm.com</p>
  <p>Email: comedian@paulvantrimm.com</p>
</section>

<p class="event">@Your Event</p>
<p class="clients-heading">Some Previous Satisfied Clients:</p>

<section class="clients">
  <span class="client"><i></i>Northway</span>
  <span class="client"><i></i>Kestrel Co.</span>
  <span class="client"><i></i>Skyline Air</span>
  <span class="client"><i></i>Forward Mutual</span>
  <span class="client"><i></i>Harbor Assurance</span>
  <span class="client"><i></i>FreshMart</span>
  <span class="client"><i></i>Maple Grill</span>
  <span class="client"><i></i>BuildHaus</span>
  <span class="client"><i></i>Tellcast</span>
  <span class="client"><i></i>Seabreeze Yacht &amp; Country Club</span>
  <span class="more">And many other companies, country clubs and associations both large and small.</span>
</section>
</body>
</html>
```